Brochure Design Project

Please design a corporate brochure for my business "Corvin Asbestos & Safety"

Specs:-
- A4 flat size, three panel front, three panel back, roll-folded to DL
- Portrait orientation
- Full colour
Updates

Please don't forget to send in your designs. I believe the competition ends in a few hours. Thank you!

Target Market(s)

Business owners, commercial/industrial building owners, real estate property managers, strata managers

Industry/Entity Type

Business

Requirements
Must have
• - Professional / modern but serious as the content is important
- Cover page in particular must stand out so it will be noticeable if sitting on someone's desk
- Good use of whitespace and not too crowded
- Heading highlighted in warm/hot colour i.e. burnt orange, all other text in black
- Font Georgia 11pt
Nice to have
• - I have uploaded our letterhead source files too - please weave in the theme/look and feel of the letterhead into the brochure if possible.

```html
<!DOCTYPE html>
<html lang="en">
<head>
<meta charset="utf-8">
<title>Corvin Asbestos &amp; Safety – Brochure Inside Spread</title>
<link href="https://fonts.googleapis.com/css2?family=Cabin:wght@700&family=Lato:wght@400&display=swap" rel="stylesheet">
<style>
  :root {
    --green: #8cc63f;
    --green-mid: #77b82a;
    --green-light: #a8d65e;
    --green-dark: #5f9e1f;
    --navy: #1c1f3d;
    --grey-text: #555a5e;
    --grey-heading: #8a8c8e;
    --paper-top: #ffffff;
    --paper-bottom: #e4e5e6;
  }
  html, body {
    margin: 0;
    padding: 0;
    width: 1200px;
    height: 848px;
    overflow: hidden;
    background: #ffffff;
  }
  .spread {
    position: relative;
    width: 1200px;
    height: 848px;
    overflow: hidden;
    background: linear-gradient(180deg, var(--paper-top) 40%, var(--paper-bottom) 100%);
    font-family: "Lato", "Helvetica Neue", Arial, sans-serif;
  }
  .header-band {
    position: absolute;
    left: 0;
    top: 0;
    width: 1200px;
    height: 380px;
  }
  .feature {
    position: absolute;
    width: 372px;
  }
  .feature-heading {
    display: flex;
    align-items: flex-start;
    gap: 8px;
    margin: 0 0 14px 0;
  }
  .feature-marker {
    flex: 0 0 auto;
    width: 58px;
    height: 62px;
  }
  .feature-title {
    font-family: "Cabin", "Gill Sans", Arial, sans-serif;
    font-weight: 700;
    font-size: 27px;
    line-height: 28px;
    margin: 6px 0 0 0;
  }
  .feature-title .title-lead {
    display: block;
    color: var(--green);
  }
  .feature-title .title-sub {
    display: inline-block;
    color: var(--grey-heading);
    border-bottom: 3px solid var(--green);
    padding-bottom: 1px;
  }
  .feature-body {
    margin: 0;
    font-size: 12.6px;
    line-height: 20.8px;
    color: var(--grey-text);
    text-align: justify;
  }
  .feature--c1r1 { left: 15px;  top: 356px; }
  .feature--c2r1 { left: 414px; top: 377px; }
  .feature--c3r1 { left: 815px; top: 356px; }
  .feature--c1r2 { left: 15px;  top: 619px; }
  .feature--c2r2 { left: 414px; top: 640px; }

  .brand-panel {
    position: absolute;
    left: 858px;
    top: 654px;
    width: 360px;
    height: 210px;
    background: #ffffff;
    transform: skewX(-2deg);
    transform-origin: bottom left;
    box-shadow: -6px 6px 14px rgba(0, 0, 0, 0.18);
  }
  .brand-name {
    position: absolute;
    left: 906px;
    top: 700px;
    width: 270px;
    display: flex;
    align-items: center;
    gap: 14px;
    font-family: "Cabin", "Gill Sans", Arial, sans-serif;
    font-weight: 700;
    font-size: 30px;
    line-height: 34px;
    color: var(--navy);
  }
  .brand-square {
    flex: 0 0 auto;
    width: 34px;
    height: 34px;
    background: var(--green);
  }
</style>
</head>
<body>
<main class="spread">

  <svg class="header-band" viewBox="0 0 1200 380" xmlns="http://www.w3.org/2000/svg">
    <defs>
      <linearGradient id="office-tone" x1="0" y1="0" x2="0" y2="1">
        <stop offset="0" stop-color="#e9eef2"/>
        <stop offset="0.55" stop-color="#d7d6cf"/>
        <stop offset="1" stop-color="#b99a72"/>
      </linearGradient>
      <linearGradient id="store-tone" x1="0" y1="0" x2="0" y2="1">
        <stop offset="0" stop-color="#cfcac2"/>
        <stop offset="0.5" stop-color="#9e948c"/>
        <stop offset="1" stop-color="#e8e6e2"/>
      </linearGradient>
      <linearGradient id="house-tone" x1="0" y1="0" x2="0" y2="1">
        <stop offset="0" stop-color="#4f8fd6"/>
        <stop offset="0.35" stop-color="#b9cde2"/>
        <stop offset="0.6" stop-color="#c9b79d"/>
        <stop offset="1" stop-color="#6f9a3c"/>
      </linearGradient>
      <clipPath id="photo-clip">
        <polygon points="0,0 1200,0 1200,214 460,330 0,252"/>
      </clipPath>
    </defs>
    <g clip-path="url(#photo-clip)">
      <rect role="img" aria-label="Photo of a bright open-plan office with staff meeting around a table" x="0" y="0" width="398" height="340" fill="url(#office-tone)"/>
      <rect role="img" aria-label="Photo of a retail clothing store interior with racks and a column" x="398" y="0" width="399" height="340" fill="url(#store-tone)"/>
      <rect role="img" aria-label="Photo of a two-storey suburban house with a garage under blue sky" x="797" y="0" width="403" height="340" fill="url(#house-tone)"/>
    </g>
    <polygon points="0,252 460,330 1200,214 1200,222 462,346 0,268" fill="var(--green-light)"/>
    <polygon points="0,268 462,346 1200,222 1200,228 462,356 0,286" fill="var(--green)"/>
    <polygon points="0,286 462,356 1200,228 1200,232 462,364 0,302" fill="var(--green-mid)"/>
  </svg>

  <section class="feature feature--c1r1">
    <h2 class="feature-heading">
      <svg class="feature-marker" viewBox="0 0 58 62" aria-hidden="true"><rect x="3" y="22" width="36" height="36" rx="5" fill="none" stroke="var(--navy)" stroke-width="5"/></svg>
      <span class="feature-title"><span class="title-lead">Lorem ipsum</span><span class="title-sub">dolor sit amet</span></span>
    </h2>
    <p class="feature-body">Lorem ipsum dolor sit amet, consectetur adipiscing elit. Duis iaculis nulla nunc, nec semper ipsum accumsan nec. Proin nec vulputate sem. Nulla condimentum a lacus ac bibendum. Duis odio magna, aliquet ac blandit vel, dapibus ac odio. Nullam eget dolor non nulla pellentesque viverra. Nulla et sagittis tortor. Pellentesque risus risus, tempor in vestibulum a, ullamcorper vel augue. Sed ut libero odio.</p>
  </section>

  <section class="feature feature--c2r1">
    <h2 class="feature-heading">
      <svg class="feature-marker" viewBox="0 0 58 62" aria-hidden="true"><rect x="3" y="22" width="36" height="36" rx="5" fill="none" stroke="var(--navy)" stroke-width="5"/></svg>
      <span class="feature-title"><span class="title-lead">Lorem ipsum</span><span class="title-sub">dolor sit amet</span></span>
    </h2>
    <p class="feature-body">Lorem ipsum dolor sit amet, consectetur adipiscing elit. Duis iaculis nulla nunc, nec semper ipsum accumsan nec. Proin nec vulputate sem. Nulla condimentum a lacus ac bibendum. Duis odio magna, aliquet ac blandit vel, dapibus ac odio. Nullam eget dolor non nulla pellentesque viverra. Nulla et sagittis tortor. Pellentesque risus risus, tempor in vestibulum a, ullamcorper vel augue. Sed ut libero odio.</p>
  </section>

  <section class="feature feature--c3r1">
    <h2 class="feature-heading">
      <svg class="feature-marker" viewBox="0 0 58 62" aria-hidden="true"><rect x="3" y="22" width="36" height="36" rx="5" fill="none" stroke="var(--navy)" stroke-width="5"/></svg>
      <span class="feature-title"><span class="title-lead">Lorem ipsum</span><span class="title-sub">dolor sit amet</span></span>
    </h2>
    <p class="feature-body">Lorem ipsum dolor sit amet, consectetur adipiscing elit. Duis iaculis nulla nunc, nec semper ipsum accumsan nec. Proin nec vulputate sem. Nulla condimentum a lacus ac bibendum. Duis odio magna, aliquet ac blandit vel, dapibus ac odio. Nullam eget dolor non nulla pellentesque viverra. Nulla et sagittis tortor. Pellentesque risus risus, tempor in vestibulum a, ullamcorper vel augue. Sed ut libero odio.</p>
  </section>

  <section class="feature feature--c1r2">
    <h2 class="feature-heading">
      <svg class="feature-marker" viewBox="0 0 58 62" aria-hidden="true"><rect x="3" y="22" width="36" height="36" rx="5" fill="none" stroke="var(--navy)" stroke-width="5"/></svg>
      <span class="feature-title"><span class="title-lead">Lorem ipsum</span><span class="title-sub">dolor sit amet</span></span>
    </h2>
    <p class="feature-body">Lorem ipsum dolor sit amet, consectetur adipiscing elit. Duis iaculis nulla nunc, nec semper ipsum accumsan nec. Proin nec vulputate sem. Nulla condimentum a lacus ac bibendum. Duis odio magna, aliquet ac blandit vel, dapibus ac odio. Nullam eget dolor non nulla pellentesque viverra.</p>
  </section>

  <section class="feature feature--c2r2">
    <h2 class="feature-heading">
      <svg class="feature-marker" viewBox="0 0 58 62" aria-hidden="true"><rect x="3" y="22" width="36" height="36" rx="5" fill="none" stroke="var(--navy)" stroke-width="5"/></svg>
      <span class="feature-title"><span class="title-lead">Lorem ipsum</span><span class="title-sub">dolor sit amet</span></span>
    </h2>
    <p class="feature-body">Lorem ipsum dolor sit amet, consectetur adipiscing elit. Duis iaculis nulla nunc, nec semper ipsum accumsan nec. Proin nec vulputate sem. Nulla condimentum a lacus ac bibendum. Duis odio magna, aliquet ac blandit vel, dapibus ac odio. Nullam eget dolor non nulla pellentesque viverra.</p>
  </section>

  <div class="brand-panel" aria-hidden="true"></div>
  <p class="brand-name"><span class="brand-square" aria-hidden="true"></span><span>Corvin Asbestos &amp; Safety</span></p>

</main>
</body>
</html>
```